Engineering Consultant Business Card

I'm starting a new business as a high-end engineering consultant in a niche field. I've attached the jpg for my logo plus the branding guideline document that I've been following. You can see my business website here: www.tarvikworks.com
I'd like a business card that has the logo on one side, then the other side has (in any order): Tarvik Works, Inc.
Dana Whitlock
President and Chief EMC Engineer
www.tarvikworks.com
dana@tarvikworks.com
Optional: motto "We will solve your EMC problems as early as possible—ideally before they even start."
I'm not planning on including a phone number
Target Market(s)
Businesses, especially makers of electronics hardware
Industry/Entity Type
Electrical engineering
Contact Information for Business Card
Company name, my name, website, email

```html
<!DOCTYPE html>
<html lang="en">
<head>
<meta charset="utf-8">
<title>Tarvik Works, Inc. – Business Card</title>
<link rel="stylesheet" href="https://fonts.googleapis.com/css2?family=Inter:wght@500;600;700&family=Source+Serif+4:wght@400&display=swap">
<style>
  :root {
    --backdrop: #c3c3c3;
    --brand-blue: #2a43a0;
    --brand-sky: #7cc4d4;
    --ink-navy: #2a2a8c;
    --ink-black: #111111;
    --paper: #ffffff;
  }
  html, body {
    margin: 0;
    padding: 0;
    width: 1200px;
    height: 1200px;
    overflow: hidden;
    background: var(--backdrop);
  }
  .canvas {
    position: relative;
    width: 1200px;
    height: 1200px;
    font-family: "Inter", Arial, sans-serif;
  }
  .card {
    position: absolute;
    left: 226px;
    width: 746px;
    height: 436px;
    border-radius: 25px;
    overflow: hidden;
  }
  /* Front */
  .card-front {
    top: 118px;
    background: var(--brand-blue);
  }
  .brand-lockup {
    position: absolute;
    left: 0;
    right: 0;
    top: 0;
    height: 382px;
    display: flex;
    align-items: center;
    justify-content: center;
    gap: 20px;
  }
  .brand-dot {
    width: 46px;
    height: 46px;
    border-radius: 50%;
    border: 8px solid var(--paper);
    box-sizing: border-box;
  }
  .brand-name {
    color: var(--paper);
    font-weight: 700;
    font-size: 62px;
    letter-spacing: -0.5px;
  }
  .web-band {
    position: absolute;
    left: 0;
    right: 0;
    bottom: 0;
    height: 54px;
    background: var(--brand-sky);
    color: var(--paper);
    font-weight: 700;
    font-size: 21px;
    display: flex;
    align-items: center;
    justify-content: center;
  }
  /* Back */
  .card-back {
    top: 611px;
    background: var(--paper);
  }
  .contact {
    position: absolute;
    left: 0;
    right: 0;
    top: 128px;
    text-align: center;
  }
  .person-name {
    margin: 0;
    color: var(--brand-sky);
    font-weight: 600;
    font-size: 30px;
    line-height: 1;
  }
  .person-title {
    margin: 12px 0 0;
    color: var(--ink-black);
    font-weight: 700;
    font-size: 13.5px;
    letter-spacing: 0.6px;
    text-transform: uppercase;
  }
  .person-email {
    display: inline-block;
    margin-top: 30px;
    color: var(--ink-navy);
    font-weight: 500;
    font-size: 23px;
    text-decoration: none;
    padding-bottom: 4px;
    border-bottom: 2px solid var(--ink-navy);
  }
  .motto-band {
    position: absolute;
    left: 0;
    right: 0;
    bottom: 0;
    height: 113px;
    background: linear-gradient(180deg, #2b44a2 0%, #283f98 100%);
    display: flex;
    align-items: center;
    justify-content: center;
  }
  .motto {
    margin: 0;
    color: var(--paper);
    font-family: "Source Serif 4", Georgia, serif;
    font-size: 21px;
    line-height: 1.25;
    text-align: center;
  }
</style>
</head>
<body>
<main class="canvas">
  <section class="card card-front" aria-label="Card front">
    <div class="brand-lockup">
      <span class="brand-dot" aria-hidden="true"></span>
      <span class="brand-name">Tarvik Works</span>
    </div>
    <div class="web-band">www.tarvikworks.com</div>
  </section>

  <section class="card card-back" aria-label="Card back">
    <div class="contact">
      <h1 class="person-name">Dana Whitlock</h1>
      <p class="person-title">President and Chief EMC Engineer</p>
      <a class="person-email" href="mailto:dana@tarvikworks.com">dana@tarvikworks.com</a>
    </div>
    <div class="motto-band" role="img" aria-label="Faint circuit schematic pattern behind the motto">
      <p class="motto">“We will solve your EMC problems as early as possible—<br>ideally before they even start."</p>
    </div>
  </section>
</main>
</body>
</html>
```